We are full service plumbing contractors that are capable of performing all of your plumbing need...

A clean, crisp website that conveys we can handle any plumbing from drain cleaning, repairs, to new construction. But emphasis on Leak detection, under-slab and underground water service leaks, repairs, and reroutes. Leak detection by acoustical, Thermal, or tracer gas , methods.Also emphasize advanced drain cleaning technologies and equipment. Don't just poke ahole in the drain blockage, Clean the pipe, with our High pressure hydrojetters, or Chain knocker drain cables that expand to the width of the pipe being cleaned.

Number of Pages Required

5+ page

Font styles to use
Sans Serif

Requirements
Should not have
• Canned photos

```html
<!DOCTYPE html>
<html lang="en">
<head>
<meta charset="utf-8">
<title>Flowline Crew – Plumbing Contractors</title>
<link rel="stylesheet" href="https://fonts.googleapis.com/css2?family=Montserrat:wght@500;700;800&family=PT+Sans:ital,wght@0,400;0,700;1,400&display=swap">
<style>
:root{
  --navy:#161a5c;
  --blue:#1472c4;
  --red:#e31b37;
  --ink:#1d1d1f;
  --body:#4a4a4a;
  --muted:#9a9a9a;
  --line:#e4e4e4;
  --white:#ffffff;
  --dark:#2a2725;
}
*{box-sizing:border-box;margin:0;padding:0}
html,body{width:1200px;height:3175px;overflow:hidden;background:var(--white)}
body{position:relative;font-family:"PT Sans",Arial,sans-serif;color:var(--body)}
.abs{position:absolute}
.heading{font-family:"Montserrat",Arial,sans-serif;font-weight:700;color:var(--ink);letter-spacing:.5px}

/* header */
.site-header{left:161px;top:21px;width:878px;height:70px;background:var(--white);box-shadow:0 2px 8px rgba(0,0,0,.08)}
.brand{left:14px;top:18px;display:flex;align-items:center;gap:8px;font-family:"Montserrat",Arial,sans-serif;font-weight:800;font-size:19px;color:var(--navy)}
.brand-dot{width:14px;height:14px;border-radius:50%;background:var(--blue)}
.main-nav{left:264px;top:0;height:70px;display:flex;align-items:center;gap:46px;font-family:"PT Sans",Arial,sans-serif;font-size:11px;text-transform:uppercase;color:var(--muted)}
.main-nav .active{color:var(--blue);font-weight:700}
.quick-call{left:732px;top:0;width:146px;height:70px;background:var(--navy);color:var(--white);text-align:center;padding-top:14px}
.quick-call .num{font-family:"Montserrat",Arial,sans-serif;font-weight:700;font-size:15px}
.quick-call .lab{font-style:italic;font-size:14px;margin-top:3px}

/* hero */
.hero-photo{left:0;top:0;width:1200px;height:740px;background:linear-gradient(100deg,#dfe3e1 0%,#c4c9c7 35%,#b7b3ae 60%,#8e8782 80%,#c8c8c6 100%)}
.hero-fade{left:0;top:560px;width:1200px;height:180px;background:linear-gradient(180deg,rgba(255,255,255,0),#fff)}
.hero-panel{left:438px;top:199px;width:326px;height:389px;background:rgba(120,120,120,.55)}
.hero-kicker{left:0;top:252px;width:1200px;text-align:center;font-style:italic;font-size:14px;color:var(--navy)}
.hero-title{left:0;top:282px;width:1200px;text-align:center;font-family:"Montserrat",Arial,sans-serif;font-weight:700;font-size:58px;line-height:68px;color:#101010}
.btn-red{left:548px;top:491px;width:102px;height:40px;background:var(--red);color:var(--white);font-family:"Montserrat",Arial,sans-serif;font-weight:700;font-size:10px;text-transform:uppercase;display:flex;align-items:center;justify-content:center}
.scroll-mark{left:583px;top:778px;width:32px;height:32px;background:var(--navy);transform:rotate(45deg)}
.scroll-arrow{left:591px;top:786px}

/* section titles */
.title-block{width:76px;height:68px;background:var(--blue)}
.title-block::after{content:"";position:absolute;left:8px;top:8px;width:76px;height:68px;border:2px solid var(--blue)}
.section-title{font-family:"Montserrat",Arial,sans-serif;font-weight:700;font-size:26px;color:var(--ink);text-transform:uppercase}

/* about */
.about-text{left:161px;top:1018px;width:400px;font-size:11.5px;line-height:21px;color:#333;font-weight:700}
.about-text p+p{margin-top:16px}
.link-more{left:161px;top:1196px;font-family:"Montserrat",Arial,sans-serif;font-weight:700;font-size:10px;color:var(--blue);text-transform:uppercase;display:flex;align-items:center;gap:8px}
.about-photo{left:586px;top:910px;width:455px;height:292px;border-radius:38% 20% 30% 24% / 22% 30% 24% 34%;background:radial-gradient(circle at 50% 60%,#a66f4d 0%,#7b4f35 55%,#c9c0b3 100%)}
.rule{left:0;top:1287px;width:1200px;height:1px;background:var(--line)}

/* services */
.service{top:1477px;width:210px;height:135px;padding-left:14px;border-left:2px solid #d8d8d8}
.service:first-of-type{border-left:0}
.service h3{font-family:"Montserrat",Arial,sans-serif;font-weight:700;font-size:11px;color:var(--ink);margin:8px 0 6px 10px;text-transform:uppercase}
.service p{font-size:11px;line-height:19px;color:#444}
.dots{left:585px;top:1640px;width:32px;height:3px;display:flex;gap:4px}
.dots span{flex:1;background:var(--navy)}
.dots span+span{background:#9aa0b5}

/* more services */
.tools-photo{left:0;top:1672px;width:1200px;height:613px;background:linear-gradient(180deg,#fff 0%,#d9d9d7 20%,#cfcecb 60%,#fff 100%)}
.subtitle{left:261px;top:1826px;font-size:12px;font-weight:700;color:var(--ink)}
.tile{width:176px;height:146px;background:var(--navy);color:var(--white);padding:24px 18px 0}
.tile span{display:block;margin-top:16px;font-size:11.5px;line-height:19px}

/* testimonials */
.quote-card{top:2455px;width:421px;height:165px;background:var(--white);box-shadow:0 2px 10px rgba(0,0,0,.12);padding:22px 30px}
.quote-mark{font-family:Georgia,serif;font-size:60px;line-height:40px;color:#d5d5d5;height:40px}
.quote-card p{font-size:11px;line-height:19px;color:#444;margin-top:8px}
.quote-card h4{font-size:12px;color:var(--ink);margin-top:16px}

/* contact */
.contact-photo{left:0;top:2687px;width:1200px;height:407px;background:linear-gradient(110deg,#1f1c1a 0%,#4a3a32 35%,#3a3633 60%,#1a1a1a 100%)}
.contact-shade{left:0;top:2687px;width:1200px;height:407px;background:rgba(0,0,0,.35)}
.contact-title{color:var(--white)}
.field{top:2858px;color:#ddd;font-size:11px;border-bottom:1px solid #aaa;height:24px}
.field-wide{left:161px;top:2908px;width:630px;height:40px;color:#ddd;font-size:11px;border-bottom:1px solid #aaa}
.btn-submit{left:163px;top:3000px;width:82px;height:39px;background:var(--blue);color:var(--white);font-family:"Montserrat",Arial,sans-serif;font-weight:700;font-size:10px;display:flex;align-items:center;justify-content:center}
.contact-info{left:857px;color:var(--white);font-size:11px;line-height:17px;display:flex;gap:16px}
.contact-info b{font-family:"Montserrat",Arial,sans-serif;font-size:10px}

/* footer */
.site-footer{left:0;top:3094px;width:1200px;height:81px;background:var(--white)}
.foot-brand{left:164px;top:28px}
.foot-nav{left:330px;top:33px;font-size:11px;color:var(--ink)}
.socials{left:716px;top:33px;display:flex;gap:10px}
.socials span{width:11px;height:11px;border-radius:50%;background:var(--blue)}
.copyright{left:876px;top:26px;font-size:10.5px;line-height:15px;color:var(--muted)}
</style>
</head>
<body>

<!-- hero -->
<div class="abs hero-photo" role="img" aria-label="Kitchen sink with plumbing tools, pipe wrenches and hoses"></div>
<div class="abs hero-fade"></div>
<div class="abs hero-panel"></div>
<div class="abs hero-kicker">Flowline Crew</div>
<h1 class="abs hero-title">READY TO SERVICE ALL<br>YOUR PLUMBING NEEDS!</h1>
<div class="abs btn-red">Learn More</div>

<header class="abs site-header">
  <div class="abs brand"><span class="brand-dot"></span>Flowline Crew</div>
  <nav class="abs main-nav">
    <span class="active">Home</span><span>About Us</span><span>Services</span><span>Testimonials</span><span>Contact Us</span>
  </nav>
  <div class="abs quick-call"><div class="num">+1 555 010 2040</div><div class="lab">Quick Call</div></div>
</header>

<div class="abs scroll-mark"></div>
<svg class="abs scroll-arrow" width="16" height="16" viewBox="0 0 16 16"><path d="M8 3v9M5 9l3 3 3-3" stroke="#fff" stroke-width="1.6" fill="none"/></svg>

<!-- about -->
<div class="abs title-block" style="left:161px;top:920px"></div>
<h2 class="abs section-title" style="left:195px;top:938px">About Us</h2>
<div class="abs about-text">
  <p>We handle every plumbing job, from drain cleaning and repairs to new construction. Our crews specialise in leak detection for under-slab and underground water lines, with quick repairs and clean reroutes that last.</p>
  <p>We find hidden leaks using acoustic, thermal and tracer gas methods, so we dig only where the problem really is.</p>
</div>
<div class="abs link-more">Learn More
  <svg width="14" height="8" viewBox="0 0 14 8"><path d="M0 4h12M9 1l3 3-3 3" stroke="#1472c4" stroke-width="1.5" fill="none"/></svg>
</div>
<div class="abs about-photo" role="img" aria-label="Excavated underground water service line with a copper valve"></div>
<div class="abs rule"></div>

<!-- services -->
<div class="abs title-block" style="left:161px;top:1366px"></div>
<h2 class="abs section-title" style="left:193px;top:1384px">Our Services</h2>

<div class="abs service" style="left:161px;border-left:0">
  <svg width="60" height="32" viewBox="0 0 60 32"><rect x="4" y="10" width="40" height="12" rx="6" fill="none" stroke="#161a5c" stroke-width="3"/><path d="M44 16h12M20 22v8" stroke="#161a5c" stroke-width="3"/></svg>
  <h3>Hydro Jetting</h3>
  <p>High pressure water scours the full pipe wall and clears grease, scale and roots.</p>
</div>
<div class="abs service" style="left:387px">
  <svg width="40" height="36" viewBox="0 0 40 36"><path d="M8 4h12v16h12v10" stroke="#161a5c" stroke-width="6" fill="none"/></svg>
  <h3>Leak Detection</h3>
  <p>Acoustic, thermal and tracer gas tools locate slab and underground leaks fast.</p>
</div>
<div class="abs service" style="left:614px">
  <svg width="40" height="36" viewBox="0 0 40 36"><path d="M8 2v18a8 8 0 0 0 16 0V12h10" stroke="#161a5c" stroke-width="3" fill="none"/></svg>
  <h3>Drain Cleaning</h3>
  <p>Chain knocker cables expand to the pipe width to clean, not just poke through.</p>
</div>
<div class="abs service" style="left:840px">
  <svg width="44" height="36" viewBox="0 0 44 36"><path d="M6 18h32M22 6v12M14 6h16" stroke="#161a5c" stroke-width="5" fill="none"/><path d="M8 18v14M36 18v14" stroke="#161a5c" stroke-width="5"/></svg>
  <h3>Mainline Replacements</h3>
  <p>Worn or broken main lines replaced and rerouted with minimal digging on site.</p>
</div>
<div class="abs dots"><span></span><span></span></div>

<!-- more services -->
<div class="abs tools-photo" role="img" aria-label="Plumbing tools, tape measure and fittings laid out on a work surface"></div>
<div class="abs title-block" style="left:161px;top:1774px"></div>
<h2 class="abs section-title" style="left:186px;top:1792px">More Services</h2>
<div class="abs subtitle">Other services we offer include:</div>

<div class="abs tile" style="left:163px;top:1890px"><svg width="40" height="32" viewBox="0 0 40 32"><path d="M4 10h22M14 4v6M26 10v16" stroke="#fff" stroke-width="5" fill="none"/></svg><span>Buried line<br>Locatio</span></div>
<div class="abs tile" style="left:391px;top:1890px"><svg width="40" height="32" viewBox="0 0 40 32"><path d="M8 2v16a8 8 0 0 0 16 0V8h10" stroke="#fff" stroke-width="4" fill="none"/></svg><span>ADA fixture<br>Conversions</span></div>
<div class="abs tile" style="left:620px;top:1890px"><svg width="40" height="32" viewBox="0 0 40 32"><path d="M4 14h32M20 4v10M12 4h16M6 14v14M34 14v14" stroke="#fff" stroke-width="4" fill="none"/></svg><span>Mainline<br>Replacements</span></div>
<div class="abs tile" style="left:163px;top:2059px"><svg width="50" height="32" viewBox="0 0 50 32"><rect x="4" y="10" width="30" height="10" rx="5" fill="none" stroke="#fff" stroke-width="3"/><path d="M34 15h12M16 20v8" stroke="#fff" stroke-width="3"/></svg><span>Hydro<br>Jetting</span></div>
<div class="abs tile" style="left:391px;top:2059px"><svg width="40" height="32" viewBox="0 0 40 32"><path d="M8 2v16a8 8 0 0 0 16 0V10h10" stroke="#fff" stroke-width="3" fill="none"/></svg><span>Drain<br>Clenning</span></div>
<div class="abs tile" style="left:620px;top:2059px"><svg width="40" height="32" viewBox="0 0 40 32"><path d="M10 4h12v14h10v10" stroke="#fff" stroke-width="5" fill="none"/></svg><span>Leck<br>Detection</span></div>

<!-- testimonials -->
<div class="abs title-block" style="left:163px;top:2340px"></div>
<h2 class="abs section-title" style="left:188px;top:2358px">Waht Our Client Says</h2>
<div class="abs quote-card" style="left:163px">
  <div class="quote-mark">&ldquo;</div>
  <p>They found the slab leak in an hour and fixed it the same day. Clean, fast work.</p>
  <h4>Dana Reyes</h4>
</div>
<div class="abs quote-card" style="left:616px">
  <div class="quote-mark">&ldquo;</div>
  <p>Our old drain finally runs clear after the hydro jetting. Honest price and friendly crew.</p>
  <h4>Dana Reyes</h4>
</div>

<!-- contact -->
<div class="abs contact-photo" role="img" aria-label="Plumber tightening a pipe fitting with a wrench"></div>
<div class="abs contact-shade"></div>
<div class="abs title-block" style="left:163px;top:2752px"></div>
<h2 class="abs section-title contact-title" style="left:193px;top:2770px">Contact Us</h2>

<div class="abs field" style="left:161px;width:150px">Phone :</div>
<div class="abs field" style="left:351px;width:150px">E-mail :</div>
<div class="abs field" style="left:537px;width:254px">Letter or Physical Meet-Up :</div>
<div class="abs field-wide">Address :</div>
<div class="abs btn-submit">SUBMIT</div>

<div class="abs contact-info" style="top:2858px">
  <svg width="14" height="14" viewBox="0 0 14 14"><path d="M3 1l2.5 3-1.5 1.5a8 8 0 0 0 4.5 4.5L10 8.5l3 2.5-1.5 2C6 13 1 8 1 2.5z" fill="#fff"/></svg>
  <div><b>CALL US :</b><br>+1 555 010 2040</div>
</div>
<div class="abs contact-info" style="top:2912px">
  <svg width="14" height="12" viewBox="0 0 14 12"><rect x="1" y="1" width="12" height="10" fill="none" stroke="#fff" stroke-width="1.4"/><path d="M1 1l6 5 6-5" stroke="#fff" stroke-width="1.4" fill="none"/></svg>
  <div><b>EMAIL US :</b><br>hello@flowlinecrew.example</div>
</div>

<!-- footer -->
<footer class="abs site-footer">
  <div class="abs brand foot-brand"><span class="brand-dot"></span>Flowline Crew</div>
  <div class="abs foot-nav">Home &nbsp;|&nbsp; Services &nbsp;|&nbsp; Testimonials &nbsp;|&nbsp; About Us &nbsp;|&nbsp; Contact Us</div>
  <div class="abs socials"><span></span><span></span><span></span><span></span></div>
  <div class="abs copyright">Copyright 2019 &copy;<br>Flowline Crew. All Rights Reserved.</div>
</footer>

</body>
</html>
```